Dynamic Business Card for Sports Supplements Company

Hi! I'm looking for an awesome business card to match my existing sports supplement company. I have uploaded my current company logo and screenshot of the front page of my website.

I would like to have something dynamic and interesting and utilize the colors in the website - the reds and purples

The business card should be double sided and focus on a unique eye-catching design on the back and include all the relevant company info.

Most importantly, it should say somewhere: "Sign up on our website for a coupon code."

Target Market(s)

Mostly for women gym goers but it shouldn't be too feminine. It should be in keeping with the website design. It should flow and clearly be connected to it

Industry/Entity Type

Business

Contact Information for Business Card

Colleen M. Varga
CEO
CVarga@Vitalorexco.example
www.vitalorexco.example
555.014.3827
P.O. Box 48317
Alderwick, Kestrel 00000

Sign up on our website for a coupon code

Font styles to use
Serif
Sans Serif
Other font styles liked:
• Novecento font family and "Vitalorex" is in AR Destine font

Requirements
Must have
• One side should be a bold Vitalorex logo design. Even just the symbol itself may be o.k. (see attached file)

```html
<!DOCTYPE html>
<html lang="en">
<head>
<meta charset="utf-8">
<title>Vitalorex Business Card</title>
<link rel="stylesheet" href="https://fonts.googleapis.com/css2?family=Roboto:ital,wght@0,400;0,700;0,900;1,700&display=swap">
<style>
  :root {
    --red: #e8232a;
    --red-deep: #b3161c;
    --black: #141414;
    --white: #ffffff;
    --purple: #7b3f9e;
    --ink: #1a1a1a;
    --rule: #555555;
    --backdrop: #3a3a3c;
  }
  * { margin: 0; padding: 0; box-sizing: border-box; }
  html, body { width: 1200px; height: 900px; overflow: hidden; }
  body {
    background: var(--backdrop);
    font-family: "Roboto", Arial, sans-serif;
    position: relative;
  }
  .card {
    position: absolute;
    left: 300px;
    width: 600px;
    height: 344px;
    overflow: hidden;
    box-shadow: 0 10px 30px rgba(0,0,0,.45);
  }
  .card--back { top: 80px; }
  .card--front { top: 476px; background: var(--white); color: var(--ink); }

  .back-artwork {
    position: absolute; inset: 0;
    background: linear-gradient(150deg, var(--red) 0%, var(--red) 55%, var(--red-deep) 100%);
  }
  .back-badge {
    position: absolute;
    left: 230px; top: 102px;
    width: 140px; height: 140px;
    border-radius: 50%;
    background: var(--black);
    border: 6px solid var(--white);
    display: flex; align-items: center; justify-content: center;
    color: var(--white);
    font-weight: 900;
    font-size: 24px;
    letter-spacing: .5px;
  }

  .holder { position: absolute; left: 40px; top: 34px; }
  .holder__name { font-weight: 700; font-style: italic; font-size: 17px; }
  .holder__role { font-weight: 700; font-style: italic; font-size: 14px; color: var(--red); margin-top: 2px; }

  .divider {
    position: absolute; left: 40px; right: 40px; top: 190px;
    height: 1px; background: var(--rule);
  }

  .contact { position: absolute; left: 40px; top: 118px; list-style: none; font-size: 14px; line-height: 21px; }
  .contact li { display: flex; align-items: center; gap: 8px; }
  .contact svg { width: 12px; height: 12px; flex: none; }

  .brand-notch { position: absolute; left: 414px; top: 0; width: 70px; height: 34px; }
  .brand { position: absolute; right: 40px; top: 94px; text-align: right; }
  .brand__name { font-weight: 900; font-size: 42px; letter-spacing: 1px; color: var(--black); line-height: 1; }
  .brand__tagline { font-size: 11px; letter-spacing: 2.6px; text-transform: uppercase; margin-top: 6px; }

  .address { position: absolute; right: 40px; top: 204px; text-align: right; font-size: 16px; line-height: 22px; font-style: normal; }

  .promo-band { position: absolute; left: 0; top: 282px; width: 600px; height: 40px; }
  .promo-band__text {
    position: absolute; left: 66px; right: 80px; top: 282px; height: 40px;
    display: flex; align-items: center; justify-content: center;
    color: var(--white); font-size: 16px; font-weight: 400; letter-spacing: .3px;
  }
</style>
</head>
<body>

  <section class="card card--back" aria-label="Card back">
    <div class="back-artwork" role="img" aria-label="Bold red and black diagonal stripe artwork"></div>
    <div class="back-badge">Vitalorex</div>
  </section>

  <section class="card card--front" aria-label="Card front">
    <div class="holder">
      <p class="holder__name">Colleen M. Varga</p>
      <p class="holder__role">CEO</p>
    </div>

    <ul class="contact">
      <li>
        <svg viewBox="0 0 12 12" aria-hidden="true"><path d="M2.5 1 4.5 1 5.3 3.6 4 4.6C4.7 6 6 7.3 7.4 8L8.4 6.7 11 7.5 11 9.5C11 10.3 10.3 11 9.5 11 5 11 1 7 1 2.5 1 1.7 1.7 1 2.5 1Z" fill="var(--red)"/></svg>
        555.014.3827
      </li>
      <li>
        <svg viewBox="0 0 12 12" aria-hidden="true"><rect x="0.5" y="2" width="11" height="8" fill="var(--red)"/><path d="M0.5 2 6 6.5 11.5 2" stroke="var(--white)" stroke-width="1" fill="none"/></svg>
        CVarga@Vitalorexco.example
      </li>
      <li>
        <svg viewBox="0 0 12 12" aria-hidden="true"><circle cx="6" cy="6" r="5.2" fill="none" stroke="var(--red)" stroke-width="1.3"/><path d="M1 6H11M6 1V11M6 1C3.5 3.5 3.5 8.5 6 11M6 1C8.5 3.5 8.5 8.5 6 11" stroke="var(--red)" stroke-width="1" fill="none"/></svg>
        www.vitalorexco.example
      </li>
    </ul>

    <div class="divider"></div>

    <svg class="brand-notch" viewBox="0 0 70 34" aria-hidden="true">
      <polygon points="0,0 70,0 35,34" fill="var(--black)"/>
    </svg>

    <div class="brand">
      <p class="brand__name">Vitalorex</p>
      <p class="brand__tagline">Your training ally</p>
    </div>

    <address class="address">
      P.O. Box 48317<br>
      Alderwick, Kestrel 00000
    </address>

    <svg class="promo-band" viewBox="0 0 600 40" aria-hidden="true">
      <polygon points="14,8 30,4 34,20 22,30 10,24" fill="var(--purple)"/>
      <polyline points="40,10 48,20 40,30" fill="none" stroke="var(--black)" stroke-width="4"/>
      <polyline points="50,10 58,20 50,30" fill="none" stroke="var(--black)" stroke-width="4"/>
      <polygon points="66,6 520,6 534,20 520,34 66,34" fill="var(--black)"/>
      <polyline points="552,10 544,20 552,30" fill="none" stroke="var(--black)" stroke-width="4"/>
      <polyline points="562,10 554,20 562,30" fill="none" stroke="var(--black)" stroke-width="4"/>
      <polygon points="572,12 586,8 592,22 582,32 568,26" fill="var(--purple)"/>
    </svg>
    <p class="promo-band__text">Sign up on our website for a coupon code</p>
  </section>

</body>
</html>
```